Redesign Video/PIcture Check in Page

Redesign our current TallyPointApp iPhone App checkin screens - Keep the design simple so that programmers do not have to do too much extra work to make your design work. - Look at the attached website screenshot for the overall look and feel, and color scheme - Convert the attached vector logo to iOS Icon format. - Deliver all graphics in the density required for iPhone XS Max. I will upload current check in pages that need to be reimagined. Check in needs to be more intutitive. Would like to add some gamification to the verification screen where they currently are required to enter series of random numbers. simple card game etc might work better. See TallyPointapp in itunes and google play store. also visit vormlink.example or tallypointapp.example for more information about our company.
The Current Checkin Process:
A. Client receives alert to checkin or submits voluntary checkin
B. Clicks checkin button on home Screen.
Redesign from here:
C. Clicks on a check in from check in list screen(new screen)
D. Enters verification number(gamification something better than random numbers)
E. Opens Camera
D. Takes Selfie
F. submits photo
G. clicks check in
SEE CURRENT STEPS PIC I UPLOADED

Target Market(s)

Courts,Probation and parole,Attorneys,Sheriffs,Jails, Alternative sentencing

Colors
3277b5

Requirements
Must have
• Must be easy to navigate,Intuitive!
Nice to have
• Gamification of check in verification.
• Step by step process with next button or similar

```html
<!DOCTYPE html>
<html lang="en">
<head>
<meta charset="utf-8">
<title>Check in – Verification Screens</title>
<link rel="stylesheet" href="https://fonts.googleapis.com/css2?family=Inter:wght@200;300;400;500;600&display=swap">
<style>
  :root {
    --navy: #0a2d6e;
    --accent: #3277b5;
    --ink: #3a3a3a;
    --muted: #a8a8a8;
    --line: #c9ccd3;
    --tab-muted: #9a9a9a;
    --button-idle: #c8c8c8;
    --page: #f7f8fb;
    --screen: #ffffff;
    --alert: #f0362b;
  }
  * { box-sizing: border-box; margin: 0; padding: 0; }
  html, body {
    width: 1200px; height: 1200px; overflow: hidden;
    background: var(--page);
    font-family: "Inter", sans-serif;
  }
  .canvas { position: relative; width: 1200px; height: 1200px; }

  .screen {
    position: absolute; top: 58px;
    width: 492px; height: 1066px;
    background: var(--screen);
    border-radius: 48px;
    box-shadow: 0 10px 40px rgba(40, 60, 110, 0.08);
    overflow: hidden;
  }
  .screen--code { left: 56px; }
  .screen--selfie { left: 614px; }

  .menu-button { position: absolute; left: 36px; top: 80px; width: 42px; height: 26px; }
  .menu-button span {
    position: absolute; left: 0; height: 3px; border-radius: 2px; background: var(--navy);
  }
  .menu-button span:nth-child(1) { top: 0; width: 42px; }
  .menu-button span:nth-child(2) { top: 11px; width: 36px; }
  .menu-button span:nth-child(3) { top: 22px; width: 30px; }

  .user-name {
    position: absolute; right: 110px; top: 80px;
    font-size: 15.5px; font-weight: 600; color: var(--ink); letter-spacing: -0.2px;
  }
  .user-avatar {
    position: absolute; left: 404px; top: 60px; width: 60px; height: 60px; border-radius: 50%;
    background: radial-gradient(circle at 45% 45%, #8a7362, #4a3d35 70%, #6f6a66);
    box-shadow: 0 2px 6px rgba(0,0,0,0.15);
  }

  .page-title {
    position: absolute; left: 34px; top: 140px;
    font-size: 61px; font-weight: 200; color: var(--navy); letter-spacing: -3px;
  }
  .request-title {
    position: absolute; left: 50px; top: 247px;
    font-size: 21px; font-weight: 600; color: var(--ink); letter-spacing: -0.3px;
  }
  .request-time {
    position: absolute; left: 50px; top: 276px;
    font-size: 15.5px; font-weight: 500; color: var(--muted);
  }

  .code-slot {
    position: absolute; top: 322px; width: 64px; height: 70px;
    border-bottom: 1.5px solid var(--line);
    text-align: center;
    font-size: 50px; font-weight: 200; line-height: 66px; color: var(--navy);
  }

  .tile {
    position: absolute; width: 94px; height: 94px; border-radius: 50%;
    background: var(--navy);
  }
  .tile--revealed {
    background: var(--screen);
    box-shadow: 0 14px 30px rgba(50, 119, 181, 0.14);
    text-align: center; line-height: 92px;
    font-size: 50px; font-weight: 200; color: var(--navy);
  }
  .tile--current { color: var(--accent); }

  .submit-button {
    position: absolute; left: 74px; top: 834px; width: 343px; height: 71px;
    border-radius: 36px; border: none; background: var(--button-idle);
    color: #fff; font: 600 21px "Inter", sans-serif;
    box-shadow: 0 14px 22px rgba(0,0,0,0.08);
  }

  .selfie-photo {
    position: absolute; left: 130px; top: 467px; width: 230px; height: 230px; border-radius: 40px;
    background: linear-gradient(135deg, #5c4b3f 0%, #8f7565 45%, #a89080 60%, #7b7c86 100%);
  }
  .checkin-action {
    position: absolute; left: 184px; top: 768px; width: 122px; height: 122px; border-radius: 50%;
    background: var(--screen);
    box-shadow: 0 12px 30px rgba(50, 119, 181, 0.16);
    text-align: center; padding-top: 32px;
  }
  .checkin-action svg { display: block; margin: 0 auto 12px; }
  .checkin-action span { font-size: 13.5px; font-weight: 600; color: var(--navy); }

  .tab-bar {
    position: absolute; left: 0; right: 0; top: 955px; height: 111px;
    border-top: 1.5px solid #cfcfcf;
  }
  .screen--selfie .tab-bar { top: 951px; }
  .tab {
    position: absolute; top: 20px; width: 90px; margin-left: -45px; text-align: center;
    font-size: 13.5px; font-weight: 500; color: var(--tab-muted);
  }
  .tab svg { display: block; margin: 0 auto 14px; }
  .tab--active { color: var(--navy); font-weight: 600; }
  .tab-icon { position: relative; width: 36px; height: 36px; margin: 0 auto 12px; }
  .tab-icon svg { margin: 0; }
  .alert-dot {
    position: absolute; right: 2px; top: -2px; width: 11px; height: 11px; border-radius: 50%;
    background: var(--alert);
  }
</style>
</head>
<body>
<div class="canvas">

  <!-- Verification code screen -->
  <section class="screen screen--code">
    <div class="menu-button"><span></span><span></span><span></span></div>
    <p class="user-name">Marcus L Denholm</p>
    <div class="user-avatar" role="img" aria-label="Profile photo of the user"></div>

    <h1 class="page-title">Check in</h1>
    <h2 class="request-title">Voluntary Check-in Request</h2>
    <p class="request-time">20 Oct 2018 10:27:59</p>

    <div class="code-slot" style="left:54px">9</div>
    <div class="code-slot" style="left:163px">8</div>
    <div class="code-slot" style="left:272px"></div>
    <div class="code-slot" style="left:381px"></div>

    <div class="tile" style="left:39px;top:441px"></div>
    <div class="tile tile--revealed tile--current" style="left:148px;top:441px">9</div>
    <div class="tile" style="left:257px;top:441px"></div>
    <div class="tile" style="left:366px;top:441px"></div>
    <div class="tile" style="left:39px;top:550px"></div>
    <div class="tile" style="left:148px;top:550px"></div>
    <div class="tile tile--revealed" style="left:257px;top:550px">8</div>
    <div class="tile" style="left:366px;top:550px"></div>
    <div class="tile" style="left:39px;top:659px"></div>
    <div class="tile" style="left:148px;top:659px"></div>
    <div class="tile" style="left:257px;top:659px"></div>
    <div class="tile" style="left:366px;top:659px"></div>

    <button class="submit-button">Submit</button>

    <nav class="tab-bar">
      <div class="tab" style="left:72px">
        <div class="tab-icon"><svg width="36" height="36" viewBox="0 0 36 36" fill="none" stroke="#555" stroke-width="2.2" stroke-linejoin="round"><path d="M4 17 18 5l14 12"/><path d="M8 14v17h7v-9h6v9h7V14"/></svg></div>Home</div>
      <div class="tab tab--active" style="left:188px">
        <div class="tab-icon"><svg width="36" height="36" viewBox="0 0 36 36" fill="none" stroke="#0a2d6e" stroke-width="2.2" stroke-linecap="round" stroke-linejoin="round"><path d="M16 33C9 25 6 19 6 14a10 10 0 0 1 20 0c0 2-.6 4-1.8 6.4"/><circle cx="16" cy="14" r="4"/><path d="m20 27 4 4 8-9"/></svg><span class="alert-dot"></span></div>Check-ins</div>
      <div class="tab" style="left:301px">
        <div class="tab-icon"><svg width="36" height="36" viewBox="0 0 36 36" fill="none" stroke="#555" stroke-width="2.2" stroke-linejoin="round"><path d="M3 8l10-4 10 4 10-4v24l-10 4-10-4-10 4z"/><path d="M13 4v24M23 8v24"/></svg></div>Map</div>
      <div class="tab" style="left:418px">
        <div class="tab-icon"><svg width="36" height="36" viewBox="0 0 36 36" fill="none" stroke="#555" stroke-width="2.2" stroke-linecap="round"><circle cx="18" cy="18" r="15"/><circle cx="19" cy="10.5" r="1.3" fill="#555" stroke="none"/><path d="M16 15h3l-2 11h3"/></svg></div>Info</div>
    </nav>
  </section>

  <!-- Selfie confirmation screen -->
  <section class="screen screen--selfie">
    <div class="menu-button"><span></span><span></span><span></span></div>
    <p class="user-name">Marcus L Denholm</p>
    <div class="user-avatar" role="img" aria-label="Profile photo of the user"></div>

    <h1 class="page-title">Check in</h1>
    <h2 class="request-title">Voluntary Check-in Request</h2>
    <p class="request-time">20 Oct 2018 10:27:59</p>

    <div class="code-slot" style="left:54px">9</div>
    <div class="code-slot" style="left:163px">8</div>
    <div class="code-slot" style="left:272px">K</div>
    <div class="code-slot" style="left:381px">G</div>

    <div class="selfie-photo" role="img" aria-label="Selfie photo taken for the check-in"></div>

    <div class="checkin-action">
      <svg width="32" height="36" viewBox="0 0 36 36" fill="none" stroke="#0a2d6e" stroke-width="2.4" stroke-linecap="round" stroke-linejoin="round"><path d="M16 33C9 25 6 19 6 14a10 10 0 0 1 20 0c0 2-.6 4-1.8 6.4"/><circle cx="16" cy="14" r="4"/><path d="m20 27 4 4 8-9"/></svg>
      <span>Check-ins</span>
    </div>

    <nav class="tab-bar">
      <div class="tab" style="left:72px">
        <div class="tab-icon"><svg width="36" height="36" viewBox="0 0 36 36" fill="none" stroke="#555" stroke-width="2.2" stroke-linejoin="round"><path d="M4 17 18 5l14 12"/><path d="M8 14v17h7v-9h6v9h7V14"/></svg></div>Home</div>
      <div class="tab tab--active" style="left:188px">
        <div class="tab-icon"><svg width="36" height="36" viewBox="0 0 36 36" fill="none" stroke="#0a2d6e" stroke-width="2.2" stroke-linecap="round" stroke-linejoin="round"><path d="M16 33C9 25 6 19 6 14a10 10 0 0 1 20 0c0 2-.6 4-1.8 6.4"/><circle cx="16" cy="14" r="4"/><path d="m20 27 4 4 8-9"/></svg><span class="alert-dot"></span></div>Check-ins</div>
      <div class="tab" style="left:301px">
        <div class="tab-icon"><svg width="36" height="36" viewBox="0 0 36 36" fill="none" stroke="#555" stroke-width="2.2" stroke-linejoin="round"><path d="M3 8l10-4 10 4 10-4v24l-10 4-10-4-10 4z"/><path d="M13 4v24M23 8v24"/></svg></div>Map</div>
      <div class="tab" style="left:418px">
        <div class="tab-icon"><svg width="36" height="36" viewBox="0 0 36 36" fill="none" stroke="#555" stroke-width="2.2" stroke-linecap="round"><circle cx="18" cy="18" r="15"/><circle cx="19" cy="10.5" r="1.3" fill="#555" stroke="none"/><path d="M16 15h3l-2 11h3"/></svg></div>Info</div>
    </nav>
  </section>

</div>
</body>
</html>
```